Design of Stationery (Business Card, Letterhead and Envelope) for Investment Company
Kestrelmoor Capital Associates Limited
Design of Stationery (Business Card, Letterhead and Envelope) for Investment Company - Financial Services
Creative Brief
Simple
Tunde A. Ibekwe
Director
7C, Dunmore Crescent, Osapa Garden Estate, Lekki Peninsula, Lagos
tunde@kestrelmoorng.example
www.kestrelmoorng.example
RC 458290
The back of the business card should have the logo of the company on navy blue background - please see the logo uploaded. Below the logo should be the words: "INVESTMENTS. ADVICE. VALUE CREATION".

```html
<!DOCTYPE html>
<html lang="en">
<head>
<meta charset="utf-8">
<title>Kestrelmoor Capital Associates – Business Card</title>
<link href="https://fonts.googleapis.com/css2?family=Open+Sans:wght@400;600;700&display=swap" rel="stylesheet">
<style>
  :root {
    --navy: #2f4a7a;
    --navy-deep: #263d66;
    --silver: #c9ccd2;
    --steel: #8d929b;
    --card: #fbfbfb;
    --ink: #2b2f36;
    --muted: #7a7f88;
    --backdrop: #e6e7e9;
    --white: #ffffff;
  }
  * { margin: 0; padding: 0; box-sizing: border-box; }
  html, body { width: 1200px; height: 901px; overflow: hidden; }
  body {
    background: var(--backdrop);
    font-family: "Open Sans", Arial, sans-serif;
    display: flex;
    align-items: center;
    justify-content: center;
    gap: 48px;
  }
  .card {
    position: relative;
    width: 520px;
    height: 300px;
    border-radius: 26px;
    background: var(--card);
    overflow: hidden;
    box-shadow: 0 6px 18px rgba(0,0,0,0.12);
  }
  .card-waves { position: absolute; inset: 0; }
  .brand {
    position: absolute;
    display: flex;
    flex-direction: column;
    color: var(--navy);
  }
  .brand-mark {
    width: 26px; height: 26px;
    background: var(--navy);
    margin-bottom: 6px;
  }
  .brand-name {
    font-weight: 600;
    font-size: 21px;
    letter-spacing: 1.5px;
    line-height: 1;
  }
  .brand-sub {
    font-weight: 600;
    font-size: 7.5px;
    letter-spacing: 3.2px;
    margin-top: 4px;
    line-height: 1;
  }
  .card-front .brand { left: 34px; top: 34px; }
  .holder {
    position: absolute;
    right: 34px; top: 56px;
    text-align: right;
  }
  .holder-name {
    font-size: 17px;
    font-weight: 400;
    letter-spacing: 0.8px;
    color: var(--ink);
    text-transform: uppercase;
  }
  .holder-role {
    font-size: 12px;
    color: var(--navy);
    margin-top: 1px;
  }
  .contact {
    position: absolute;
    right: 26px; bottom: 20px;
    list-style: none;
    color: var(--white);
    font-size: 9px;
    line-height: 13px;
    text-align: right;
  }
  .contact li { display: flex; justify-content: flex-end; align-items: center; gap: 7px; }
  .contact svg { width: 8px; height: 8px; flex: none; }
  .contact .spacer { width: 8px; }

  .card-back { background: var(--navy); }
  .card-back .brand {
    left: 50%; top: 50%;
    transform: translate(-50%, -58%);
    align-items: center;
    text-align: center;
    color: var(--white);
  }
  .card-back .brand-mark { width: 52px; height: 52px; margin-bottom: 14px; background: var(--white); }
  .card-back .brand-name { font-size: 30px; letter-spacing: 2px; }
  .card-back .brand-sub { font-size: 10px; letter-spacing: 4.6px; margin-top: 6px; }
  .tagline {
    position: absolute;
    left: 0; right: 0; bottom: 44px;
    text-align: center;
    color: var(--white);
    font-size: 10px;
    font-weight: 400;
    letter-spacing: 2.4px;
  }
</style>
</head>
<body>

  <section class="card card-front" aria-label="Business card front">
    <svg class="card-waves" viewBox="0 0 520 300" preserveAspectRatio="none" aria-hidden="true">
      <path d="M0,138 C150,100 300,205 520,150 L520,300 L0,300 Z" fill="var(--silver)"/>
      <path d="M0,156 C150,120 300,222 520,168 L520,300 L0,300 Z" fill="var(--steel)"/>
      <path d="M0,166 C150,132 300,232 520,180 L520,300 L0,300 Z" fill="var(--navy)"/>
    </svg>

    <div class="brand">
      <span class="brand-mark"></span>
      <span class="brand-name">KESTRELMOOR</span>
      <span class="brand-sub">CAPITAL ASSOCIATES</span>
    </div>

    <div class="holder">
      <p class="holder-name">Tunde A. Ibekwe</p>
      <p class="holder-role">Director</p>
    </div>

    <ul class="contact">
      <li>7C, Dunmore Crescent, Osapa Garden Estate,
        <svg viewBox="0 0 8 8"><path d="M4 0.5a2.6 2.6 0 0 1 2.6 2.6C6.6 5 4 7.6 4 7.6S1.4 5 1.4 3.1A2.6 2.6 0 0 1 4 0.5z" fill="#fff"/></svg></li>
      <li>Lekki Peninsula, Lagos <span class="spacer"></span></li>
      <li>0801 555 0142
        <svg viewBox="0 0 8 8"><rect x="2" y="0.5" width="4" height="7" rx="0.8" fill="#fff"/></svg></li>
      <li>0802 555 0187
        <svg viewBox="0 0 8 8"><rect x="2" y="0.5" width="4" height="7" rx="0.8" fill="#fff"/></svg></li>
      <li>0803 555 0163
        <svg viewBox="0 0 8 8"><rect x="2" y="0.5" width="4" height="7" rx="0.8" fill="#fff"/></svg></li>
      <li>tunde@kestrelmoorng.example
        <svg viewBox="0 0 8 8"><rect x="0.5" y="1.5" width="7" height="5" fill="#fff"/><path d="M0.5 1.5 L4 4.5 L7.5 1.5" stroke="var(--navy)" stroke-width="0.7" fill="none"/></svg></li>
      <li>www.kestrelmoorng.example
        <svg viewBox="0 0 8 8"><circle cx="4" cy="4" r="3.4" fill="none" stroke="#fff" stroke-width="0.9"/><path d="M0.6 4h6.8M4 0.6v6.8" stroke="#fff" stroke-width="0.7"/></svg></li>
    </ul>
  </section>

  <section class="card card-back" aria-label="Business card back">
    <div class="brand">
      <span class="brand-mark"></span>
      <span class="brand-name">KESTRELMOOR</span>
      <span class="brand-sub">CAPITAL ASSOCIATES</span>
    </div>
    <p class="tagline">INVESTMENTS. ADVICE. VALUE CREATION</p>
  </section>

</body>
</html>
```